Corvedo Nutrition Website Design. Turnkey ready to go live.

Create a small, basic website for Corvedo. Mimic the design attributes and graphic elements in the sales literature and PPT presentation. White chicken, various graphics found in the literature can be used.
Keep the site simple and graphic. Here's an example: https://www.pobraq.com/website-template/view/html/4271/?siteId=7a1c93d2-5e0b-4f8a-b2c6-81d9e3f4a702&metaSiteId=53816204-9d7e-4b1a-a3f5-06c2e8b7d914&originUrl=https%3A%2F%2Fwww.pobraq.com%2Fwebsite%2Ftemplates%2Fhtml%2Fdesign%2Fdesigner

Also: https://www.pobraq.com/website-template/view/html/2954/?siteId=6e8d21f7-4a3c-4b9e-8d15-c07a3f92e6b1&metaSiteId=fa3b8e17-2c6d-4f09-9e4a-b85d1c7032e8&originUrl=https%3A%2F%2Fwww.pobraq.com%2Fwebsite%2Ftemplates%2Fhtml%2Fdesign%2Fdesigner

Don't get locked into the examples. They are meant as examples of the level of simplicity we're looking for. The main goal is a fast, simple site that mimics the provided literature - executted quickly.

Target Market(s)

Animal nutrition industry: production managers of livestock grow operations.

Industry/Entity Type

Nutrition

Coding

Coded - Design and coding required

Number of Pages Required

1 page

Font styles to use
Sans Serif

Requirements
Must have
• Synergy with he provided sales literature themes. Use of the provided info graphics.
• "Call us" "email us" call to action.
• 1 (800) 555-0193
• info@corvedonutrition.example (current url at hostwick)
Nice to have
• Cool scrolling that creates an interesting visual experience. Mobile version.

```html
<!DOCTYPE html>
<html lang="en">
<head>
<meta charset="utf-8">
<title>Corvedo Nutrition — Animal Nutrition</title>
<link href="https://fonts.googleapis.com/css2?family=Poppins:wght@400;500;600;700&display=swap" rel="stylesheet">
<style>
:root{
  --teal:#16b79b;
  --teal-dark:#12a38a;
  --lime:#a9c93a;
  --yellow:#ebb71c;
  --olive:#8fae2b;
  --ink:#1d1d1d;
  --muted:#6f6f6f;
  --white:#ffffff;
  --footer:#ececec;
  --brand-grad:linear-gradient(90deg,var(--teal) 0%,var(--lime) 55%,var(--yellow) 100%);
}
*{box-sizing:border-box;margin:0;padding:0}
html,body{width:1200px;height:2927px;overflow:hidden}
body{font-family:'Poppins',Arial,sans-serif;color:var(--ink);background:var(--white);position:relative}

/* hero */
.hero{position:absolute;left:0;top:0;width:1200px;height:580px;overflow:hidden}
.hero-photo{position:absolute;inset:0;background:
  radial-gradient(ellipse 380px 300px at 480px 230px,#7a4b28 0%,#5a3a22 45%,rgba(60,50,30,0) 100%),
  linear-gradient(180deg,#3c4a36 0%,#4b4a34 45%,#3f5a2c 100%)}
.hero-shade{position:absolute;inset:0;background:rgba(20,20,15,.45)}
.brand{position:absolute;left:146px;top:36px;font-size:38px;font-weight:500;color:var(--white)}
.hero-phone{position:absolute;left:864px;top:48px;display:flex;align-items:center;gap:14px;color:var(--white);font-size:20px;font-weight:600}
.hero-title{position:absolute;left:0;width:1200px;top:258px;text-align:center;color:var(--white);font-size:70px;font-weight:600;line-height:1}
.hero-sub{position:absolute;left:0;width:1200px;top:332px;text-align:center;color:var(--white);font-size:31px;font-weight:600}
.btn{position:absolute;height:48px;border-radius:24px;background:var(--brand-grad);color:var(--white);font-size:19px;font-weight:600;display:flex;align-items:center;justify-content:center}
.btn-call{left:400px;top:402px;width:188px}
.btn-mail{left:611px;top:402px;width:188px}
.slider-dots{position:absolute;top:519px;left:544px;display:flex;gap:14px}
.slider-dots span{width:16px;height:16px;border-radius:50%;border:2px solid var(--white)}
.slider-dots span.on{border-color:var(--teal)}

/* benefit band */
.benefits{position:absolute;left:0;top:580px;width:1200px;height:302px;background:var(--brand-grad)}
.benefit{position:absolute;top:70px;width:240px;text-align:center;color:var(--white);font-size:15px;font-weight:600;line-height:1.35}
.benefit svg{display:block;margin:0 auto 22px}

/* trial stats */
.section-title{position:absolute;left:0;width:1200px;text-align:center;font-weight:600}
.trial-title{top:946px;font-size:26px;color:var(--lime)}
.trial-title span{color:var(--teal)}
.stat{position:absolute;width:220px;text-align:center}
.stat-ring{width:172px;height:172px;margin:0 auto;border:3px solid var(--teal-dark);border-radius:50%;display:flex;flex-direction:column;align-items:center;justify-content:center;gap:12px}
.stat-num{font-size:38px;font-weight:600;color:var(--teal-dark);line-height:1}
.stat-label{margin-top:22px;font-size:21px;font-weight:600}
.stat-sub{margin-top:2px;font-size:11px;color:#444}

/* feed vs water */
.effects{position:absolute;left:0;top:1360px;width:1200px;height:868px;background:var(--brand-grad)}
.effects-title{top:74px;font-size:25px;color:var(--white)}
.effect-copy{position:absolute;width:425px;color:var(--white)}
.effect-copy h3{font-size:21px;font-weight:600;margin-bottom:26px}
.effect-copy p{font-size:11.5px;line-height:1.8;opacity:.95}
.monitor{position:absolute;width:347px}
.monitor-bezel{background:#1f1f1f;border-radius:8px 8px 0 0;padding:12px 14px 12px}
.monitor-screen{background:var(--white);height:176px}
.monitor-chin{height:34px;background:linear-gradient(180deg,#e9e9e9,#c9c9c9);border-radius:0 0 8px 8px}
.monitor-neck{width:96px;height:30px;margin:0 auto;background:linear-gradient(180deg,#bdbdbd,#e6e6e6)}
.monitor-foot{width:160px;height:8px;margin:0 auto;background:#d4d4d4;border-radius:4px 4px 0 0}

/* gut health */
.gut-title{position:absolute;left:146px;top:2350px;font-size:25px;font-weight:600;color:var(--teal)}
.gut-title span{color:var(--lime)}
.gut-copy{position:absolute;left:146px;top:2432px;width:508px;font-size:11.5px;line-height:1.8;color:var(--muted)}
.gut-copy p+p{margin-top:18px}
.btn-more{left:146px;top:2687px;width:188px;height:48px;font-size:15px}
.ingredient-graphic{position:absolute;left:686px;top:2318px;width:410px;height:420px;border-radius:50%;background:radial-gradient(circle at 50% 50%,#ffffff 0%,#f1f7f4 55%,#dcefe8 100%)}
.cycle-list{position:absolute;left:771px;top:2438px;width:240px;text-align:center;font-size:12.5px;font-weight:700;line-height:1.25;letter-spacing:.4px}
.cycle-list li{list-style:none;margin-bottom:13px}

/* footer */
.site-footer{position:absolute;left:0;top:2819px;width:1200px;height:108px;background:var(--footer)}
.footer-brand{position:absolute;left:146px;top:28px;font-size:36px;font-weight:500;color:var(--teal)}
.footer-copy{position:absolute;left:335px;top:45px;font-size:12px;color:#333}
.socials{position:absolute;left:858px;top:42px;display:flex;gap:11px}
.socials span{width:22px;height:22px;border-radius:50%;border:1.5px solid var(--olive)}
</style>
</head>
<body>

<header class="hero">
  <div class="hero-photo" role="img" aria-label="Photo of a brown hen standing in a green farmyard"></div>
  <div class="hero-shade"></div>
  <div class="brand">Corvedo</div>
  <div class="hero-phone">
    <svg width="24" height="24" viewBox="0 0 24 24" aria-hidden="true"><path d="M6.6 10.8a15 15 0 0 0 6.6 6.6l2.2-2.2a1 1 0 0 1 1-.25 11.4 11.4 0 0 0 3.6.57 1 1 0 0 1 1 1V20a1 1 0 0 1-1 1A17 17 0 0 1 3 4a1 1 0 0 1 1-1h3.5a1 1 0 0 1 1 1c0 1.25.2 2.45.57 3.57a1 1 0 0 1-.25 1z" fill="none" stroke="#ffffff" stroke-width="1.8"/></svg>
    <span>1 (800) 555-0193</span>
  </div>
  <h1 class="hero-title">Animal Nutrition</h1>
  <p class="hero-sub">Health starts &amp; ends with the gut</p>
  <a class="btn btn-call">Call Us</a>
  <a class="btn btn-mail">E-Mail</a>
  <div class="slider-dots"><span class="on"></span><span></span><span></span><span></span></div>
</header>

<section class="benefits">
  <div class="benefit" style="left:169px">
    <svg width="64" height="56" viewBox="0 0 64 56" fill="none" stroke="#fff" stroke-width="2"><path d="M20 54V20M32 54V12M44 54V20"/><path d="M20 28l-6-5M20 36l-6-5M32 20l-6-5M32 28l6-5M44 28l6-5M44 36l6-5"/></svg>
    Positively influence growth performance,Intestinal microbial balance and liver health
  </div>
  <div class="benefit" style="left:469px">
    <svg width="64" height="56" viewBox="0 0 64 56" fill="none" stroke="#fff" stroke-width="2"><circle cx="32" cy="22" r="14"/><path d="M32 36v18M22 54h20"/></svg>
    Relievs weaning stress, prevents diarrhea and promotes growth
  </div>
  <div class="benefit" style="left:791px">
    <svg width="64" height="56" viewBox="0 0 64 56" fill="none" stroke="#fff" stroke-width="2"><path d="M32 4l20 8v14c0 14-9 24-20 28C21 50 12 40 12 26V12z"/><path d="M24 28l6 6 11-12"/></svg>
    Combats pathogenic bacteria and fungi,reducing spoilage
  </div>
</section>

<section>
  <h2 class="section-title trial-title"><span>Veltrazyme</span> USA heat stress trial Summary</h2>
  <div class="stat" style="left:138px;top:1042px">
    <div class="stat-ring"><span class="stat-num">3%</span><svg width="16" height="10" viewBox="0 0 16 10"><path d="M2 2l6 6 6-6" fill="none" stroke="#1d1d1d" stroke-width="2.6"/></svg></div>
    <div class="stat-label">Increased</div><div class="stat-sub">Weight Gain</div>
  </div>
  <div class="stat" style="left:372px;top:1042px">
    <div class="stat-ring"><span class="stat-num">5.8%</span><svg width="16" height="10" viewBox="0 0 16 10"><path d="M2 2l6 6 6-6" fill="none" stroke="#1d1d1d" stroke-width="2.6"/></svg></div>
    <div class="stat-label">Decreased</div><div class="stat-sub">Feed Conversion Ratio</div>
  </div>
  <div class="stat" style="left:606px;top:1042px">
    <div class="stat-ring"><span class="stat-num">55%</span><svg width="16" height="10" viewBox="0 0 16 10"><path d="M2 2l6 6 6-6" fill="none" stroke="#1d1d1d" stroke-width="2.6"/></svg></div>
    <div class="stat-label">Decreased</div><div class="stat-sub">Lession Scores</div>
  </div>
  <div class="stat" style="left:840px;top:1042px">
    <div class="stat-ring"><span class="stat-num">48%</span><svg width="16" height="10" viewBox="0 0 16 10"><path d="M2 2l6 6 6-6" fill="none" stroke="#1d1d1d" stroke-width="2.6"/></svg></div>
    <div class="stat-label">Decreased</div><div class="stat-sub">Mortality Rate</div>
  </div>
</section>

<section class="effects">
  <h2 class="section-title effects-title">Effects of Feed vs Water Application</h2>

  <div class="effect-copy" style="left:146px;top:192px">
    <h3>Body Weight Gain(kg)</h3>
    <p>Birds given the blend in feed or water gained more weight than the control group across the trial, and the best gain came when both routes were used together through the hottest weeks of the season. Growers saw even flocks, steady intake and stronger birds at the end of the cycle, with less day to day variation between houses and sites.</p>
  </div>
  <div class="monitor" style="left:611px;top:148px">
    <div class="monitor-bezel"><div class="monitor-screen">
      <svg width="319" height="176" viewBox="0 0 319 176" font-family="Arial, sans-serif">
        <g stroke="#e2e2e2" stroke-width="1"><path d="M40 20H300M40 38H300M40 56H300M40 74H300M40 92H300M40 110H300M40 128H300"/></g>
        <g font-size="6" fill="#999"><text x="20" y="22">3.15</text><text x="20" y="58">3.05</text><text x="20" y="94">2.95</text><text x="20" y="130">2.85</text></g>
        <rect x="55" y="104" width="34" height="38" fill="#8fae2b"/><text x="72" y="99" text-anchor="middle" font-size="14" font-weight="700" fill="#8fae2b">2.93</text>
        <rect x="120" y="50" width="34" height="92" fill="#8dcbe8"/><text x="137" y="45" text-anchor="middle" font-size="14" font-weight="700" fill="#8dcbe8">3.08</text>
        <rect x="180" y="50" width="34" height="92" fill="#5ab3df"/><text x="197" y="45" text-anchor="middle" font-size="14" font-weight="700" fill="#5ab3df">3.08</text>
        <rect x="240" y="42" width="34" height="100" fill="#16a593"/><text x="257" y="37" text-anchor="middle" font-size="14" font-weight="700" fill="#16a593">3.11</text>
        <g fill="none" stroke="#fff" stroke-width="1"><circle cx="137" cy="100" r="11"/><circle cx="197" cy="100" r="11"/><circle cx="257" cy="96" r="11"/></g>
        <g font-size="6" fill="#fff" text-anchor="middle"><text x="137" y="102">5.1%</text><text x="197" y="102">5.1%</text><text x="257" y="98">6.1%</text></g>
        <g font-size="7" fill="#333" text-anchor="middle"><text x="72" y="153">Control</text><text x="137" y="153">Feed</text><text x="197" y="153">Water</text><text x="257" y="153">Feed</text><text x="257" y="162">and</text><text x="257" y="171">water</text></g>
      </svg>
    </div></div>
    <div class="monitor-chin"></div><div class="monitor-neck"></div><div class="monitor-foot"></div>
  </div>

  <div class="monitor" style="left:166px;top:492px">
    <div class="monitor-bezel"><div class="monitor-screen">
      <svg width="319" height="176" viewBox="0 0 319 176" font-family="Arial, sans-serif">
        <g stroke="#e2e2e2" stroke-width="1"><path d="M40 20H300M40 38H300M40 56H300M40 74H300M40 92H300M40 110H300M40 128H300"/></g>
        <g font-size="6" fill="#999"><text x="20" y="22">1.92</text><text x="20" y="58">1.88</text><text x="20" y="94">1.84</text><text x="20" y="130">1.80</text></g>
        <rect x="55" y="30" width="34" height="112" fill="#8fae2b"/><text x="72" y="25" text-anchor="middle" font-size="14" font-weight="700" fill="#8fae2b">1.90</text>
        <rect x="120" y="76" width="34" height="66" fill="#8dcbe8"/><text x="137" y="71" text-anchor="middle" font-size="14" font-weight="700" fill="#8dcbe8">1.85</text>
        <rect x="180" y="85" width="34" height="57" fill="#5ab3df"/><text x="197" y="80" text-anchor="middle" font-size="14" font-weight="700" fill="#5ab3df">1.84</text>
        <rect x="240" y="94" width="34" height="48" fill="#16a593"/><text x="257" y="89" text-anchor="middle" font-size="14" font-weight="700" fill="#16a593">1.83</text>
        <g fill="none" stroke="#fff" stroke-width="1"><circle cx="137" cy="110" r="11"/><circle cx="197" cy="114" r="11"/><circle cx="257" cy="120" r="11"/></g>
        <g font-size="6" fill="#fff" text-anchor="middle"><text x="137" y="112">-2.6%</text><text x="197" y="116">-3.2%</text><text x="257" y="122">-3.7%</text></g>
        <g font-size="7" fill="#333" text-anchor="middle"><text x="72" y="153">Control</text><text x="137" y="153">Feed</text><text x="197" y="153">Water</text><text x="257" y="153">Feed</text><text x="257" y="162">and</text><text x="257" y="171">water</text></g>
      </svg>
    </div></div>
    <div class="monitor-chin"></div><div class="monitor-neck"></div><div class="monitor-foot"></div>
  </div>

  <div class="effect-copy" style="left:546px;top:546px">
    <h3>Feed Conversion Ratio</h3>
    <p>Feed conversion improved in every treated group, so each bird needed less feed for each kilo of gain. Combining feed and water delivery gave the lowest ratio of the trial and the clearest return for growers. Lower feed use per bird means lower cost per flock, and the gains held steady even under strong heat stress.</p>
  </div>
</section>

<section>
  <h2 class="gut-title">A Comprehensive <span>solution to gut health</span></h2>
  <div class="gut-copy">
    <p>Our blend brings seaweed extracts, chelated minerals, antioxidants, vitamins, brewer's yeast and fermentation metabolites together in one program that supports a balanced gut from the first day of placement to the last day of the grow-out cycle.</p>
    <p>A healthy gut absorbs more nutrients, resists pathogens and copes better with heat and weaning stress. The result is stronger growth, fewer losses and better feed use, which helps production managers meet their targets with confidence in every flock and every season.</p>
  </div>
  <a class="btn btn-more">Learn More</a>

  <div class="ingredient-graphic" role="img" aria-label="Infographic: ring of six ingredient icons around the list of blend components"></div>
  <ul class="cycle-list">
    <li style="color:#1f3f45">SEAWEED<br>EXTRACTS</li>
    <li style="color:#16a593">CHELATION/<br>COMPLEXATION</li>
    <li style="color:#8fae2b">ANTIOXIDANTS</li>
    <li style="color:#a9c93a">VITAMINS</li>
    <li style="color:#d9a81a">BREWER'S YEAST</li>
    <li style="color:#3a9ad0">FERMENTATION<br>METABOLITES</li>
  </ul>
</section>

<footer class="site-footer">
  <div class="footer-brand">Corvedo</div>
  <div class="footer-copy">©2018 Company Name &nbsp;|&nbsp; All Rights Reserved</div>
  <div class="socials"><span></span><span></span><span></span><span></span><span></span><span></span></div>
</footer>

</body>
</html>
```